Looking for a Lumora Book Cover

My book has been online for a while and I am now looking for a professional cover for it as it has been very well received.

You can view the book here and all the details about it:

https://www.pagevaultshop.example/dp/X7Q2KRMTPL#readerNotes

Not sure what I am looking for as a design, just open to your ideas.

I want something different that will stand out please.

Thanks
Owen

```html
<!DOCTYPE html>
<html lang="en">
<head>
<meta charset="UTF-8">
<title>Roots and Resilience — Book Cover</title>
<link rel="stylesheet" href="https://fonts.googleapis.com/css2?family=Abril+Fatface&family=Damion&family=Yellowtail&family=Archivo:wght@800;900&family=Source+Serif+4:ital,wght@0,400;1,700&display=swap">
<style>
  :root {
    --cream: #fdf0d5;
    --peach: #fddcaa;
    --orange: #d9783e;
    --rust: #a8481c;
    --umber: #5a200a;
    --ink: #0d0a07;
    --teal: #3a8f73;
  }
  html, body {
    margin: 0;
    padding: 0;
    width: 750px;
    height: 1200px;
    overflow: hidden;
    background: var(--cream);
  }
  .cover {
    position: relative;
    width: 750px;
    height: 1200px;
    background: var(--cream);
    overflow: hidden;
  }
  .artwork {
    position: absolute;
    left: 0;
    top: 0;
    width: 750px;
    height: 1200px;
  }
  .title {
    position: absolute;
    left: 138px;
    top: 40px;
    margin: 0;
    color: var(--ink);
    font-family: "Abril Fatface", serif;
    font-weight: 400;
    line-height: 1;
  }
  .title-line {
    display: block;
    font-size: 87px;
    letter-spacing: -2.5px;
    line-height: 68px;
  }
  .title-roots { margin-top: 22px; }
  .title-and {
    position: absolute;
    left: 298px;
    top: -22px;
    font-family: "Damion", "Yellowtail", cursive;
    font-weight: 400;
    font-size: 112px;
    letter-spacing: -2px;
    line-height: 1;
  }
  .tagline {
    position: absolute;
    left: 142px;
    top: 208px;
    width: 474px;
    margin: 0;
    color: var(--teal);
    font-family: "Archivo", sans-serif;
    font-weight: 900;
    font-size: 18px;
    letter-spacing: 6px;
    line-height: 27px;
    text-transform: uppercase;
  }
  .tagline-line {
    display: block;
    white-space: nowrap;
    text-align: justify;
    text-align-last: justify;
  }
  .subtitle {
    position: absolute;
    left: 82px;
    top: 914px;
    margin: 0;
    white-space: nowrap;
    color: var(--ink);
    font-family: "Source Serif 4", serif;
    font-weight: 400;
    font-size: 39px;
    letter-spacing: -1.8px;
    line-height: 40px;
  }
  .subtitle em {
    color: var(--teal);
    font-style: italic;
    font-weight: 700;
  }
  .author {
    position: absolute;
    left: 0;
    width: 750px;
    top: 1156px;
    margin: 0;
    text-align: center;
    color: var(--ink);
    font-family: "Archivo", sans-serif;
    font-weight: 800;
    font-size: 22.5px;
    letter-spacing: 0.4px;
    text-transform: uppercase;
  }
</style>
</head>
<body>
<main class="cover">
  <svg class="artwork" viewBox="0 0 750 1200" role="img" aria-label="Sepia-toned photo of a thoughtful boy in a cap resting his chin on his hand, set over a textured orange map of Africa">
    <defs>
      <filter id="rough" x="-5%" y="-5%" width="110%" height="110%">
        <feTurbulence type="fractalNoise" baseFrequency="0.035" numOctaves="3" seed="4"/>
        <feDisplacementMap in="SourceGraphic" scale="26"/>
      </filter>
      <filter id="soft"><feGaussianBlur stdDeviation="10"/></filter>
      <linearGradient id="splash" x1="0" y1="0" x2="1" y2="0.4">
        <stop offset="0" stop-color="#b9521f"/>
        <stop offset="0.4" stop-color="#eaa062"/>
        <stop offset="1" stop-color="#f7c48a"/>
      </linearGradient>
      <radialGradient id="shadowLeft" cx="0.5" cy="0.5" r="0.5">
        <stop offset="0" stop-color="#3d1405"/>
        <stop offset="0.6" stop-color="#8a3612" stop-opacity="0.8"/>
        <stop offset="1" stop-color="#c8652d" stop-opacity="0"/>
      </radialGradient>
      <linearGradient id="photo" x1="0" y1="0" x2="1" y2="1">
        <stop offset="0" stop-color="#c8652d"/>
        <stop offset="0.5" stop-color="#a4471b"/>
        <stop offset="1" stop-color="#6e2a0c"/>
      </linearGradient>
      <linearGradient id="land" x1="0" y1="0" x2="0" y2="1">
        <stop offset="0" stop-color="#fdd49a"/>
        <stop offset="1" stop-color="#fee3b8"/>
      </linearGradient>
    </defs>
    <path filter="url(#rough)" fill="url(#splash)" d="M0 380 C40 360 70 375 80 370 L110 340 C150 330 190 320 250 318 C300 312 330 305 350 310 L420 320 C500 330 560 345 600 360 C650 340 700 350 750 345 L750 880 C700 870 660 890 600 900 C520 880 470 830 420 800 C380 780 330 790 280 810 C230 835 170 850 120 860 C80 850 40 840 0 830 Z"/>
    <ellipse cx="90" cy="560" rx="170" ry="170" fill="url(#shadowLeft)" filter="url(#soft)"/>
    <path filter="url(#rough)" fill="url(#photo)" d="M360 330 C420 315 500 320 540 360 C560 420 540 480 560 530 C610 560 680 600 750 640 L750 880 C700 875 660 890 620 900 C560 880 500 840 440 810 C400 790 330 780 300 770 C285 700 290 620 320 560 C345 500 360 430 360 330 Z"/>
    <path filter="url(#rough)" fill="url(#land)" d="M300 770 C340 760 390 770 440 790 C500 810 560 860 620 900 C680 920 720 900 750 890 L750 1200 L375 1200 C370 1120 355 1040 340 980 C320 900 290 830 300 770 Z"/>
  </svg>

  <h1 class="title">
    <span class="title-line title-roots">ROOTS</span>
    <span class="title-and">and</span>
    <span class="title-line">RESILIENCE</span>
  </h1>

  <p class="tagline">
    <span class="tagline-line">A Celebration of Culture,</span>
    <span class="tagline-line">Struggle and Achievement</span>
  </p>

  <p class="subtitle">The <em>History, Resistance</em> and<br><em>Excellence</em> of Black People<br><em>in Africa</em> and the Diaspora</p>

  <p class="author">Everett Lankford</p>
</main>
</body>
</html>
```